Product brochure for KRF Plans and Voip Telephone Systems

Our company recently added KRF internet and fuly managed cloud hosted VOIP telephony system into our product line. We need a brochure designed that we can put on our website and also print out and take to potential client meetings to showcase our offiering. The brochure will need to describe our details of our voip system and 3 KRF speed offering along with pricing. This brochure will also need to incorporate our company logo which can be found on our website www.silverpondit.com.au
We are essentially looking for an overall brochure template that we can add in the details and pricing after. Winning designer will need to provide all original modifiable vectors/files. We would also like to turn the winning design into a template for a page on our website to showcase our product.
Our 7VQ voip telephone system is used by some of the largest corporations in the world. More details can be found at 7vq-example.com
Small to medium businesses and large enterprises.
Internet

```html
<!DOCTYPE html>
<html lang="en">
<head>
<meta charset="utf-8">
<title>Quillmarsh Technology – Voip Telephone Systems</title>
<link href="https://fonts.googleapis.com/css2?family=Carlito:wght@400;700&display=swap" rel="stylesheet">
<style>
  :root {
    --red: #d0171c;
    --ink: #1c1c1c;
    --grey-light: #f4f4f4;
    --grey-mid: #dcdcdc;
    --grey-dark: #8a8a8a;
    --footer: #0a0a0a;
    --white: #ffffff;
  }
  * { margin: 0; padding: 0; box-sizing: border-box; }
  html, body { width: 831px; height: 1200px; overflow: hidden; background: var(--white); }
  .brochure {
    position: relative; width: 831px; height: 1200px; overflow: hidden;
    font-family: "Carlito", "Calibri", Arial, sans-serif; color: var(--ink);
  }
  .brand {
    position: absolute; top: 28px; left: 70px;
    display: flex; align-items: center; gap: 18px;
  }
  .brand-square { width: 62px; height: 62px; background: var(--ink); }
  .brand-name { font-weight: 700; font-size: 54px; letter-spacing: 1px; color: var(--ink); line-height: 1; }
  .page-title {
    position: absolute; top: 143px; left: 145px;
    font-weight: 700; font-size: 44px; color: var(--ink);
  }
  .title-rule {
    position: absolute; top: 204px; left: 140px; width: 560px; height: 4px;
    background: linear-gradient(90deg, var(--grey-dark) 0%, var(--red) 45%, var(--red) 60%, var(--grey-mid) 100%);
  }
  .feature-box {
    position: absolute; top: 263px; left: 28px; width: 305px; height: 207px;
    background: linear-gradient(180deg, var(--white), var(--grey-light));
    border-radius: 6px; box-shadow: 4px 6px 10px rgba(0,0,0,0.3);
    padding: 22px 0 0 34px;
  }
  .feature-list { list-style: none; }
  .feature-list li {
    font-size: 28px; line-height: 42px; position: relative; padding-left: 28px;
  }
  .feature-list li::before {
    content: ""; position: absolute; left: 2px; top: 18px;
    width: 9px; height: 9px; border-radius: 50%; background: var(--red);
  }
  .product-visual {
    position: absolute; top: 262px; left: 355px; width: 462px; height: 185px;
    background: radial-gradient(ellipse at center, #5a5a5a 0%, #2a2a2a 55%, #e8e8e8 100%);
    border-radius: 4px;
  }
  .section-heading {
    position: absolute; left: 60px; font-weight: 700; font-size: 27px; color: var(--red);
  }
  .body-copy {
    position: absolute; left: 60px; width: 760px; font-size: 27px; line-height: 44px;
  }
  .voip-heading { top: 517px; }
  .voip-copy { top: 556px; }
  .pricing-panel {
    position: absolute; top: 734px; left: 38px; width: 760px; height: 222px;
    background: linear-gradient(180deg, var(--grey-mid), var(--grey-light) 40%, var(--white));
    border-left: 4px solid var(--red); border-radius: 6px;
    box-shadow: 2px 4px 8px rgba(0,0,0,0.25);
  }
  .pricing-heading { top: 744px; }
  .pricing-copy { top: 780px; }
  .closing-copy { top: 975px; left: 52px; }
  .site-footer {
    position: absolute; bottom: 0; left: 0; width: 831px; height: 134px;
    background: var(--footer); color: var(--white); padding: 10px 0 0 10px;
  }
  .footer-name { font-weight: 700; font-size: 25px; color: var(--red); line-height: 32px; }
  .footer-line { font-size: 21px; line-height: 30px; }
</style>
</head>
<body>
<div class="brochure">
  <header class="brand">
    <span class="brand-square"></span>
    <span class="brand-name">QUILLMARSH TECHNOLOGY</span>
  </header>

  <h1 class="page-title">Voip Telephone Systems</h1>
  <div class="title-rule"></div>

  <div class="feature-box">
    <ul class="feature-list">
      <li>Lorem ipsum dolor</li>
      <li>Lorem ipsum dolor</li>
      <li>Lorem ipsum dolor</li>
      <li>Lorem ipsum dolor</li>
    </ul>
  </div>

  <div class="product-visual" role="img" aria-label="Product photo of VoIP desk phones and a video phone"></div>

  <h2 class="section-heading voip-heading">Voip Telephone Systems</h2>
  <p class="body-copy voip-copy">Lorem ipsum dolor sit amet, consectetur adipiscing elit, sed do eiusmod tempor incididunt ut labore et dolore magna aliqua. Ut enim ad minim veniam, quis nostrud exercitation ullamco laboris nisi ut aliquip ex ea commodo consequat.</p>

  <div class="pricing-panel"></div>
  <h2 class="section-heading pricing-heading">Pricing Area</h2>
  <p class="body-copy pricing-copy">Lorem ipsum dolor sit amet, consectetur adipiscing elit, sed do eiusmod tempor incididunt ut labore et dolore magna aliqua. Ut enim ad minim veniam, quis nostrud exercitation ullamco laboris nisi ut aliquip ex ea commodo consequat.</p>

  <p class="body-copy closing-copy">Lorem ipsum dolor sit amet, consectetur adipiscing elit, sed do eiusmod tempor incididunt ut labore et dolore magna aliqua.</p>

  <footer class="site-footer">
    <p class="footer-name">Quillmarsh Technology</p>
    <p class="footer-line">Tel: +61 8 8000 4521</p>
    <p class="footer-line">Postal: PO Box 4410 Fernvale NT 0899, Australia</p>
    <p class="footer-line">Email: enquiries@quillmarsh-example.com.au</p>
  </footer>
</div>
</body>
</html>
```